電子書籍の表紙デザインを以下の内容で作成していただけると幸いです。 ◆タイトル 子育てに疲れちゃっているお母さんへ ぽかぽか家族のつくりかた! どうしようもない怒りをコントロール出来る方法 ◆サブタイトル 勉強よりももっと大切な事を知って、 人間関係をスムーズにしよう! ◆その他の文言(入れても入れなくてOKです) ・「怒りのタイプ別診断テスト」付き ・20年間の児童養護施設勤務の経験者が語る ・なぜ、⾃分の⼤切な子どもを虐待するのか? ・お⺟さんの笑顔が家族の幸せ ・怒りは悪いことではありません。 ◆著者名 堀井 達郎 ◆2点お願いがあります! 1:添付のロゴをどこかに使ってください。 2:下記文言を小さく右下に入れてください。 あまり目立たないようにお願いします。 「moTAシリーズ第2弾 事業再構築 外-2」 ちなみに、第一弾はこちらでした↓ https://www.hondana-shop.jp/item/Q7TR2LWP8N/ ◆イメージ 小さなお子さんのいるママ向けの本です。 怒りをコントロールできるようになって 幸せな家庭生活を送っているイメージでお願いします。 ◆注意事項 ・背景が白の場合、枠線を入れてください。 ・Pagenix ブックスタジオの表紙画像の要件を満たすように作成をお願いします。 https://studio.pagenix-books.jp/guide?pageId=M5WQ8ZRT3KD1HB どうぞよろしくお願いいたします。 |
どの案も素敵でしたが、著者様のご希望でこちらの案になりました。
皆様、ご提案ありがとうございました。
どれも素敵な案ばかりでした。
このシリーズは続きますので、次回もどうぞよろしくお願いいたします。

```html
<!DOCTYPE html>
<html lang="ja">
<head>
<meta charset="utf-8">
<title>ぽかぽか家族のつくりかた! 表紙</title>
<link rel="stylesheet" href="https://fonts.googleapis.com/css2?family=M+PLUS+Rounded+1c:wght@500;800;900&family=Noto+Sans+JP:wght@500;700;900&display=swap">
<style>
:root{
  --magenta:#e5177d;
  --red:#e0262e;
  --teal:#1aa3a8;
  --ink:#1c1c1c;
  --yellow:#fbe97a;
  --yellow-deep:#f7d917;
  --pink-soft:#fde4ee;
  --white:#ffffff;
}
*{margin:0;padding:0;box-sizing:border-box}
html,body{width:749px;height:1200px;overflow:hidden;background:var(--white)}
.cover{
  position:relative;width:749px;height:1200px;overflow:hidden;
  font-family:"Noto Sans JP",sans-serif;color:var(--ink);
  background:radial-gradient(circle at 50% 28%,var(--white) 0%,var(--white) 35%,var(--pink-soft) 100%);
}
.lead{
  position:absolute;top:36px;left:50%;transform:translateX(-50%);
  border:3px solid var(--teal);border-radius:40px;background:var(--white);
  color:var(--teal);font-weight:700;font-size:29px;padding:6px 30px;white-space:nowrap;
}
.title{
  position:absolute;top:100px;left:0;width:100%;text-align:center;
  font-family:"M PLUS Rounded 1c",sans-serif;font-weight:900;color:var(--magenta);
  -webkit-text-stroke:3px var(--white);paint-order:stroke fill;
  text-shadow:0 4px 0 rgba(229,23,125,.18);
}
.title .line1{display:block;font-size:84px;line-height:1}
.title .particle{
  display:block;width:56px;height:56px;margin:6px auto 4px;border-radius:50%;
  background:var(--yellow-deep);color:var(--magenta);font-size:34px;line-height:56px;
  -webkit-text-stroke:0;
}
.title .line2{display:block;font-size:94px;line-height:1}
.headline{
  position:absolute;top:340px;left:0;width:100%;text-align:center;
  font-weight:900;font-size:50px;line-height:1.2;letter-spacing:-1px;
}
.headline .accent{color:var(--red)}
.headline .marked{
  color:var(--red);
  background:linear-gradient(transparent 62%,var(--yellow-deep) 62%);
}
.subtitle{
  position:absolute;top:478px;left:0;width:100%;text-align:center;
  color:var(--teal);font-weight:700;font-size:24px;line-height:1.5;
}
.author{
  position:absolute;top:565px;left:0;width:100%;text-align:center;
  font-weight:700;font-size:26px;letter-spacing:4px;
}
.band{
  position:absolute;top:620px;left:0;width:100%;height:580px;background:var(--yellow);
}
.band .career{
  position:absolute;top:26px;left:24px;font-weight:900;font-size:31px;white-space:nowrap;
}
.band .message{
  position:absolute;top:78px;left:24px;color:var(--red);font-weight:900;font-size:52px;line-height:1.25;
}
.badge{
  position:absolute;top:78px;right:22px;width:140px;height:140px;background:var(--white);
  border-radius:14px;border:3px solid var(--red);text-align:center;
  display:flex;flex-direction:column;justify-content:center;
  font-weight:900;color:var(--red);font-size:25px;line-height:1.15;
}
.badge small{font-size:18px;color:var(--ink)}
.family-scene{
  position:absolute;top:250px;left:0;width:100%;height:270px;
  background:linear-gradient(180deg,var(--yellow) 0%,#f8d9a6 100%);
}
.footer{
  position:absolute;bottom:18px;left:22px;right:22px;display:flex;align-items:center;gap:14px;
}
.brand{display:flex;align-items:center;gap:6px;font-weight:900;font-size:24px;color:var(--teal)}
.brand .dot{width:22px;height:22px;border-radius:50%;background:var(--teal)}
.series-note{font-size:14px;font-weight:500;color:#555}
</style>
</head>
<body>
<main class="cover">
  <p class="lead">子育てに疲れちゃっているお母さんへ</p>
  <h1 class="title">
    <span class="line1">ぽかぽか家族</span>
    <span class="particle">の</span>
    <span class="line2">つくりかた!</span>
  </h1>
  <p class="headline">どうしようもない<span class="accent">怒り</span>を<br><span class="marked">コントロール</span>出来る方法</p>
  <p class="subtitle">勉強よりももっと大切な事を知って、<br>人間関係をスムーズにしよう!</p>
  <p class="author">堀井 達郎</p>
  <section class="band">
    <p class="career">20年間の児童養護施設勤務の経験者が語る</p>
    <p class="message">怒りは悪いことでは<br>ありません。</p>
    <div class="badge">怒りの<br>タイプ別<br>診断テスト<small>つき</small></div>
    <div class="family-scene" role="img" aria-label="笑顔で過ごす家族のイラストエリア"></div>
    <div class="footer">
      <span class="brand"><span class="dot"></span>moTA</span>
      <span class="series-note">moTAシリーズ第2弾　事業再構築 外-2</span>
    </div>
  </section>
</main>
</body>
</html>
```